Berichtslayout für Unternehmensberatung mit Schwerpunkt Softwareentwicklung für den Public Sektor
Wir sind eine Unternehmensberatung, die sich auf Softwareentwicklung für den Public Sektor spezialisiert hat (www.tqm-beratung.de). Unsere Zielgruppe sind Verwaltungen im deutschsprachigen Raum. Wir bieten für diesen Markt verschiedene Softwareprodukte an. Aus unseren Softwareprodukten werden automatische Controllingberichte erzeugt.
Company
We are a consulting company, that is specialised in softwaredevelopment regarding the public sector (www.tqm-beratung.de). Our customers are administrations all over Germany, Austria and Swiss. We offer different products to the market. One of which produces a report you can find enclosed to this project.
Aufgabenstellung
Es soll ein Berichtslayout erstellt werden.
• Das Berichtslayout muss die Informationen des Berichtsentwurfs aufnehmen können, beispielsweise Tabellen etc. (Anlage 1)
• Der Bericht enthält viel Text und viele Zahlen, weshalb auch ein Vorschlag über die Gestaltung der Tabellen enthalten sein soll. (Anlage 1)
• Das Layout kann Symbole wie den Falkmoorer Zeichen oder die Farben des Deckblatts aufnehmen (Anlage 2). Alle anderen Elemente können verändert werden.
• Schriftart muss Calibri sein.
• Das Berichtslayout soll übersichtlich und ansprechend aussehen.
• Das Berichtslayout soll, soweit möglich, nicht überladen wirken.
Der Bericht wird über jasper Reports erzeugt.
Wenn das Design in AI oder Indesign entwickelt wird, sollten wir dies verwenden können.
Task:
We need a better Layout for our report.
• The Layout has to be able to handle the informations shown in 'Anlage 1'.
• The layout can use Symbols like the 'Falkmoorer Zeichen' (Falkmoorer Sign) or colors of the covering page shown in 'Anlage 2'.
• Since the Layout has to handle a lot of numbers an text it would be nice if you could deliver a layout suggestion for those elements as well
• The Font has to be Calibri
• The Layout sould look as clean and appealing as possible.

```html
<!DOCTYPE html>
<html lang="de">
<head>
<meta charset="utf-8">
<title>Controlling 01-06/19 – Berichtslayout</title>
<link href="https://fonts.googleapis.com/css2?family=Carlito:ital,wght@0,400;0,700;1,400&display=swap" rel="stylesheet">
<style>
  :root {
    --red: #c4161c;
    --red-dark: #a81016;
    --ink: #2b2b2b;
    --muted: #555;
    --rule: #333;
    --grey-row: #d6d6d6;
    --paper: #ffffff;
    --backdrop: #e7e7e7;
    --green: #2aa843;
    --yellow: #f2c200;
  }
  * { box-sizing: border-box; margin: 0; padding: 0; }
  html, body { width: 1200px; height: 840px; overflow: hidden; }
  body {
    background: var(--backdrop);
    font-family: "Carlito", Calibri, sans-serif;
    color: var(--ink);
  }
  .spread {
    position: absolute; left: 34px; top: 20px;
    width: 1132px; height: 800px;
    display: flex;
    box-shadow: 0 6px 24px rgba(0,0,0,.18);
  }
  .page {
    position: relative; width: 566px; height: 800px;
    background: var(--paper);
    padding: 0 44px;
  }
  .page--left { background: linear-gradient(to right, #fff 88%, #ececec); }
  .page--right { background: linear-gradient(to left, #fff 90%, #efefef); }

  /* Labels */
  .label-box {
    position: absolute; left: 44px; top: 34px;
    background: var(--red); color: #fff;
    font-weight: 700; font-size: 15px; letter-spacing: .08em;
    padding: 8px 26px; text-transform: uppercase;
  }
  .label-band {
    position: absolute; left: 0; top: 36px; width: 380px;
    background: var(--red); color: #fff;
    font-weight: 700; font-size: 15px; letter-spacing: .08em; line-height: 1.25;
    padding: 10px 20px 10px 44px; text-transform: uppercase;
  }
  .section-title {
    font-weight: 700; font-size: 11.5px; letter-spacing: .05em; text-transform: uppercase;
    display: inline-block; border-bottom: 2px solid var(--red); padding-bottom: 1px;
  }

  /* Body text */
  .commentary { position: absolute; left: 44px; right: 44px; top: 90px; }
  .commentary p, .commentary li { font-size: 8.6px; line-height: 1.36; }
  .commentary p { margin-bottom: 7px; }
  .subhead { color: var(--red); font-size: 9px; margin-top: 8px; }
  .change-list { list-style: none; margin-bottom: 7px; }

  .measures { position: absolute; left: 44px; right: 44px; top: 116px; list-style: none; }
  .measures li { font-size: 8.8px; line-height: 1.38; padding-left: 10px; text-indent: -10px; margin-bottom: 2px; }
  .measures .num { color: var(--red); font-weight: 700; margin-right: 3px; }

  /* Tables */
  .resources { position: absolute; left: 44px; right: 44px; top: 214px; }
  .data-table { width: 100%; border-collapse: collapse; margin-top: 10px; font-size: 7.6px; }
  .data-table th, .data-table td { padding: 2.6px 3px; text-align: right; white-space: nowrap; }
  .data-table thead th { color: var(--red); font-weight: 400; font-size: 7px; vertical-align: bottom; border-bottom: 1px solid var(--rule); }
  .data-table .head-cell {
    background: var(--red); color: #fff; font-weight: 700; font-size: 8.4px; text-align: center;
    vertical-align: middle; border-bottom: none; padding: 8px 6px;
  }
  .data-table .group { border-left: 1px dashed #999; text-align: center; }
  .data-table tbody th { text-align: left; font-weight: 400; border-right: 1px solid var(--rule); }
  .data-table tbody td { border-bottom: 1px solid #e3e3e3; }
  .data-table tbody .sub th { padding-left: 8px; }
  .data-table .total th, .data-table .total td { font-weight: 700; border-top: 1px solid var(--rule); border-bottom: 1px solid var(--rule); }
  .data-table .saldo th, .data-table .saldo td { background: var(--grey-row); font-weight: 700; }
  .data-table tbody { border-bottom: 1px solid var(--rule); }

  .targets { position: absolute; left: 44px; right: 44px; top: 500px; }
  .legend { display: grid; grid-template-columns: 78px 1fr 1fr 1fr; row-gap: 6px; margin-top: 14px; font-size: 8.8px; align-items: center; }
  .legend .key { color: var(--muted); }
  .legend span.item { display: flex; align-items: center; gap: 5px; }
  .legend svg { flex: none; }
  .kpi-table { margin-top: 18px; }
  .kpi-table tbody th { white-space: normal; }

  /* Footer */
  .footer-meta { position: absolute; bottom: 22px; font-size: 8.5px; line-height: 1.3; color: var(--muted); }
  .footer-meta--left { left: 44px; }
  .footer-meta--right { right: 44px; }
  .page-number {
    position: absolute; bottom: 0; left: 50%; transform: translateX(-50%);
    background: var(--red); color: #fff; font-size: 9px; width: 54px; height: 22px;
    display: flex; align-items: center; justify-content: center;
  }
</style>
</head>
<body>
<main class="spread">

  <!-- Commentary page -->
  <section class="page page--left">
    <h1 class="label-box">Kommentar</h1>

    <article class="commentary">
      <h2 class="section-title">Finanzdaten</h2>

      <h3 class="subhead">PPL 07</h3>
      <p>Der PPL 07 wird sein Budget nach gegenwärtigem Stand um 12,8 Mio. € überschreiten (Land: 5,9 Mio. €, Stadt: 6,9 Mio. €).<br>
      Im Vergleich zum Controlling 01-05/2019 ergibt sich damit eine Verschlechterung in Höhe von 4,5 Mio. €. Die Verschlechterung setzt sich aus folgenden Veränderungen zusammen:</p>
      <ul class="change-list">
        <li>Erhöhung Mindereinnahmen um 2 Mio. € (Land: -1,7 / Stadt: -0,3)</li>
        <li>Reduzierung Personalmehrausgaben um 2 Mio. € (Land: -1,8 / Stadt: -0,2)</li>
        <li>Erhöhung konsumtive Mehrausgaben um 3,2 Mio. € (Land: 3,2)</li>
        <li>Erhöhung investive Mehrausgaben um 1,3 Mio. € (Stadt: 1,3)</li>
      </ul>

      <h3 class="subhead">Konsumtive Einnahmen</h3>
      <p>Bei den konsumtiven Einnahmen werden derzeit rd. 2,2 Mio. € an Mindereinnahmen prognostiziert. Die Verschlechterung um ca. 2 Mio. € im Vergleich zum letzten Controlling entsteht insbesondere dadurch, dass die noch im Controlling 01-05/2019 ausgewiesenen Mehreinnahmen für Polizeieinsätze bei Risikospielen von 1,5 Mio. € auf 1,2 Mio. € abgesenkt wurden. Im Controlling 01-04 ging man noch von Einnahmen in Höhe von 2 Mio. € aus. Des Weiteren sollen laut Ressort vorbehaltlich einer entsprechenden Gremienbefassung die voraussichtlichen Einnahmen i. H. v. 1,2 Mio. € komplett für die Auszahlung von Überstunden verwendet werden. Folglich wären sie dadurch nicht mehr als Mehreinnahmen vorhanden. Im Controlling 01-05 sollten dagegen bisher nur lediglich 0,5 Mio. € dafür verwendet werden. Gem. Haushaltsvermerk der entsprechenden Einnahme-Haushaltsstelle sind die Einnahmen allerdings bis maximal 0,5 Mio. € zur Auszahlung von Überstunden begrenzt. Es bleibt zudem abzuwarten, ob die Einnahmen überhaupt noch in 2019 eingehen.</p>
      <p>Des Weiteren haben sich die Mindereinnahmen bei den Gebühren für Feuerwehreinsätze um 0,4 Mio. € erhöht und es entstehen Mindereinnahmen in der Produktgruppe Wahlen in Höhe von 0,2 Mio. €. Laut Ressort wird die Kostenerstattung zur Wahl des Europäischen Parlaments geringer ausfallen, da aufgrund der gleichzeitig durchgeführten Wahlen nicht alle Kosten abrechnungsfähig sind. In der Produktgruppe „Öffentliche Ordnung“ haben sich die Mindereinnahmen geringfügig von 0,262 Mio. € auf 0,17 Mio. € reduziert. Im Personalbereich werden im Vergleich zum Controlling 01-05/2019 ca. 2 Mio. € weniger Personalmehrausgaben ausgewiesen. Ursächlich ist dafür laut Ressort eine fälschlicherweise doppelte Berücksichtigung von Personaleinstellungen in der Polizei.</p>

      <h3 class="subhead">Konsumtive Ausgaben</h3>
      <p>Bei den konsumtiven Ausgaben werden zum Jahresende derzeit 3,7 Mio. € an Mehrausgaben prognostiziert. Die Steigerung der Ausgaben im Vergleich zum Controlling 01-05/2019 i. H. v. 3,2 Mio. € ergibt sich insbesondere durch Mehrausgaben im Rettungsdienst. Laut Ressort liegt dies zum Großteil an den aus der Monatsabrechnung losgelösten Auszahlungen an Hilfsorganisationen. Des Weiteren stehen für den Bereich Notärzte noch Rechnungen aus. Die Jahreseinschätzung der Einsatzzahlen im Rettungsdienst liegt um circa 10 % unter den Jahresplanwerten, dennoch entstehen Mehrausgaben.</p>
      <p>Zusätzlich zu den durch das beschlossene Kapazitätskonzept II entstehen Bedarfe für die zusätzliche Einstellung von Studierenden im Polizeivollzug prognostiziert die Polizei zusätzliche Mehrausgaben i. H. v. 1,2 Mio. € für Geschäftsbedarf und Digitalfunkgeräte (0,57 Mio. €), DNA- und BTM-Fremdvergabe (0,270 Mio. €), Folgekosten im Rahmen des Handlungsfeldes Sichere und Saubere Stadt erworbenen Schutzausstattungen (0,215 Mio. €) sowie Dolmetscherkosten (0,145 Mio. €). Diese Mehrbedarfe wurden im letzten Controlling 01-05/2019 nicht ausgewiesen. Es ist fraglich, weshalb diese Mehrbedarfe erst jetzt ausgewiesen werden.</p>
      <p>Dem gegenüber stehen dagegen konsumtive Minderausgaben im Umfang von 1,2 Mio. € aufgrund geringerer Ausgaben für die Bürgerschafts- und Beiratswahl sowie der Europawahl. Insbesondere die Druckkosten sind laut Ressort erheblich niedriger ausgefallen, als ursprünglich vom Ressort erwartet.</p>
    </article>

    <p class="footer-meta footer-meta--left">Controlling 01-06/19<br>28.09.19</p>
    <p class="footer-meta footer-meta--right">07 Inneres</p>
    <span class="page-number">39</span>
  </section>

  <!-- Measures page -->
  <section class="page page--right">
    <h1 class="label-band">Maßnahmen-<br>Steuerungsvorschlag</h1>

    <ol class="measures">
      <li><span class="num">1</span>Das Ressort wird gebeten, die Höhe der Bedarfe aus den Kapazitätskonzepten I und II zu überprüfen und entsprechend des Beschlusses des Senats vom 30. April 2019 zunächst eine Lösung innerhalb des Produktplanbudgets sicherzustellen.</li>
      <li><span class="num">2</span>Das Ressort wird gebeten, im Controlling 01-09/2019 die konsumtiven Mehrbedarfe der Polizei, ggfs. durch Mengengerüste, detaillierter darzustellen und zu erläutern, weshalb diese Bedarfe erstmalig im Controlling 01-06/2019 dargestellt wurden.</li>
      <li><span class="num">3</span>Das Ressort wird gebeten, sämtliche Möglichkeiten zur Verbesserung der Einnahmen und zur Reduzierung der Ausgaben zu ergreifen um die Höhe der erwarteten Budgetrisiken zum Jahresende noch zu minimieren.</li>
    </ol>

    <section class="resources">
      <h2 class="section-title">Ressourceneinsatz</h2>
      <table class="data-table">
        <thead>
          <tr>
            <th class="head-cell" rowspan="2">Kamerale<br>Finanzdaten</th>
            <th colspan="4" class="group">Januar - Juni 2019</th>
            <th rowspan="2">HH-Soll</th>
            <th rowspan="2">vor. HH-Soll</th>
            <th colspan="3" class="group">Jahresplanung 2019</th>
          </tr>
          <tr>
            <th>Ist</th><th>Planwert</th><th>Abw. abs.</th><th>%</th>
            <th>vor. Ist</th><th>Abweichung</th><th>Anschlag</th>
          </tr>
        </thead>
        <tbody>
          <tr><th>Konsumtive Einnahmen</th><td>28.725</td><td>31.545</td><td>-2.819</td><td>-8,94</td><td>53.854</td><td>59.965</td><td>57.709</td><td>-2.176</td><td>58.126</td></tr>
          <tr><th>Investive Einnahmen</th><td>36</td><td>19</td><td>17</td><td>86,62</td><td>49</td><td>49</td><td>84</td><td>35</td><td>48</td></tr>
          <tr><th>Verrechnungen/Erstattungen (Einn.)</th><td>6.333</td><td>5.577</td><td>755</td><td>13,54</td><td>9.255</td><td>9.318</td><td>9.318</td><td>0</td><td>9.313</td></tr>
          <tr class="sub"><th>- Land, Stadtgem. u. intern</th><td>6.332</td><td>5.577</td><td>755</td><td>13,53</td><td>9.253</td><td>9.254</td><td>9.254</td><td>0</td><td>9.248</td></tr>
          <tr class="sub"><th>- von Falkmoorhaven</th><td>1</td><td>0</td><td>1</td><td></td><td>2</td><td>64</td><td>64</td><td>0</td><td>64</td></tr>
          <tr class="total"><th>Budgetierte Einnahmen</th><td>35.094</td><td>37.142</td><td>-2.047</td><td>-5,51</td><td>63.158</td><td>69.332</td><td>67.191</td><td>-2.141</td><td>67.487</td></tr>
          <tr><th>Personalausgaben</th><td>99.179</td><td>89.774</td><td>9.405</td><td>10,48</td><td>199.715</td><td>206.249</td><td>208.332</td><td>2.083</td><td>183.805</td></tr>
          <tr><th>Zinsausgaben</th><td>0</td><td>11</td><td>-11</td><td>-100,0</td><td>23</td><td>23</td><td>23</td><td>0</td><td>34</td></tr>
          <tr class="total"><th>Budgetierte Ausgaben</th><td>166.008</td><td>156.339</td><td>9.669</td><td>6,18</td><td>322.381</td><td>330.588</td><td>341.254</td><td>10.666</td><td>301.484</td></tr>
          <tr class="saldo"><th>SALDO</th><td>-130.914</td><td>-119.197</td><td>-11.716</td><td>9,83</td><td>-259.203</td><td>-261.256</td><td>-274.063</td><td>-12.807</td><td>-233.997</td></tr>
        </tbody>
      </table>
    </section>

    <section class="targets">
      <h2 class="section-title">Strategische Ziele / Kennzahlen / Mengengerüste</h2>

      <div class="legend">
        <span class="key">Steuerbarkeit:</span>
        <span class="item"><svg width="10" height="10"><circle cx="5" cy="5" r="4.5" fill="#333"/></svg>direkt steuerbar</span>
        <span class="item"><svg width="10" height="10"><circle cx="5" cy="5" r="4.2" fill="#fff" stroke="#333"/><path d="M5 0.8 A4.2 4.2 0 0 0 5 9.2 Z" fill="#333"/></svg>eingeschränkt steuerbar</span>
        <span class="item"><svg width="10" height="10"><circle cx="5" cy="5" r="4.2" fill="#fff" stroke="#333"/></svg>nicht steuerbar</span>
        <span class="key">Zielerreichung:</span>
        <span class="item"><svg width="10" height="10"><circle cx="5" cy="5" r="4.5" fill="var(--green)"/></svg>nicht gefährdet</span>
        <span class="item"><svg width="11" height="10"><path d="M5.5 0.5 L10.5 9.5 L0.5 9.5 Z" fill="var(--yellow)"/></svg>im Toleranzbereich</span>
        <span class="item"><svg width="10" height="10"><circle cx="5" cy="5" r="4.5" fill="var(--red)"/></svg>gefährdet</span>
      </div>

      <table class="data-table kpi-table">
        <thead>
          <tr>
            <th class="head-cell" rowspan="2">Kriminalitätsbekämpfung</th>
            <th colspan="2" class="group">Januar - Juni 2019</th>
            <th colspan="2" class="group">Ist-Plan Abweichung</th>
            <th class="group">2019</th>
            <th rowspan="2">Steuer-<br>barkeit</th>
            <th rowspan="2">Status</th>
          </tr>
          <tr>
            <th>Ist</th><th>Planwert</th><th>abs.</th><th>%</th><th>Planwert</th>
          </tr>
        </thead>
        <tbody>
          <tr><th>Leistungen</th><td></td><td></td><td></td><td></td><td></td><td></td><td></td></tr>
          <tr><th>300242 Aufklärungsquote [%]</th><td>47,50</td><td>49,00</td><td>-1,50</td><td></td><td>49,00</td><td></td><td></td></tr>
          <tr><th>300590 Anzahl strat. Ermittlungsverf. gesamt [Anz.]</th><td>38.003,000</td><td>44.250,000</td><td>-6.247,000</td><td>-14,12</td><td>88.500,000</td><td style="text-align:center"><svg width="10" height="10"><circle cx="5" cy="5" r="4.2" fill="#fff" stroke="#333"/><path d="M5 0.8 A4.2 4.2 0 0 0 5 9.2 Z" fill="#333"/></svg></td><td style="text-align:center"><svg width="11" height="10"><path d="M5.5 0.5 L10.5 9.5 L0.5 9.5 Z" fill="var(--yellow)"/></svg></td></tr>
        </tbody>
      </table>
    </section>

    <p class="footer-meta footer-meta--left">Controlling 01-06/19<br>28.09.19</p>
    <p class="footer-meta footer-meta--right">07 Inneres</p>
    <span class="page-number">41</span>
  </section>

</main>
</body>
</html>
```